Tobin Quartz Portal Page . It's guarantee project!

We need a clean and professional modern web application portal page
That includes the Login & Application Selection screen

Also, I need to design both Desktop and Mobile sizes.
We have an example design for our target

The application is Jetty Schedule and related data.
Our client is a bit conservative.

Theme color preferred : #00508B (main) #DF0D83 (secondary)

Target Market(s)

Oil & Fuel & Gasoline

Number of Pages Required

2 page

Font styles to use
Sans Serif

Colors
0054AA
0677BA
7BADD7
CADEEF
E8F1F8
E54698
E96AAD
F1A4CE
F9D9EA
FCEFF6

Requirements
Must have
• Login Page & Main Screen

```html
<!DOCTYPE html>
<html lang="en">
<head>
<meta charset="utf-8">
<title>Tobin Quartz – Log in</title>
<link rel="stylesheet" href="https://fonts.googleapis.com/css2?family=Montserrat:wght@400;500;600;700&display=swap">
<style>
  :root {
    --brand: #00508B;
    --brand-dark: #003f6e;
    --ink: #1b1b1f;
    --muted: #6b7078;
    --line: #d3d9e0;
    --field-border: #cdd4dc;
    --placeholder: #7d838b;
    --surface: #ffffff;
    --alt-icon: #7BADD7;
    --alt-icon-2: #0677BA;
  }
  * { box-sizing: border-box; margin: 0; padding: 0; }
  html, body {
    width: 1200px;
    height: 2596px;
    overflow: hidden;
    background: var(--surface);
    font-family: "Montserrat", Arial, sans-serif;
    color: var(--ink);
  }
  .screen { position: relative; width: 1200px; height: 2596px; }

  .status-bar {
    position: absolute; top: 44px; left: 0; width: 100%; height: 72px;
  }
  .status-time {
    position: absolute; left: 144px; top: 6px;
    font-size: 58px; font-weight: 600; letter-spacing: -1px;
  }
  .status-icons { position: absolute; right: 128px; top: 14px; }

  .brand-name {
    position: absolute; left: 48px; top: 292px;
    font-size: 76px; font-weight: 700; color: var(--brand); letter-spacing: -1px;
  }

  .page-title {
    position: absolute; left: 48px; top: 470px;
    font-size: 104px; font-weight: 700; line-height: 122px; letter-spacing: -1px;
  }
  .page-subtitle {
    position: absolute; left: 48px; top: 740px;
    font-size: 46px; font-weight: 500; color: var(--muted);
  }

  .social-row {
    position: absolute; left: 48px; top: 896px; width: 1104px;
    display: flex; gap: 24px;
  }
  .social-button {
    flex: 1; height: 132px;
    border: 3px solid var(--field-border); border-radius: 16px;
    display: flex; align-items: center; justify-content: center; gap: 28px;
    font-size: 54px; font-weight: 500; color: var(--ink); background: var(--surface);
  }
  .social-dot { width: 70px; height: 70px; border-radius: 50%; }
  .social-dot.first { background: var(--alt-icon); }
  .social-dot.second { background: var(--alt-icon-2); }

  .divider {
    position: absolute; left: 48px; top: 1100px; width: 1104px;
    display: flex; align-items: center; gap: 32px;
    font-size: 46px; font-weight: 500; color: var(--muted);
  }
  .divider::before, .divider::after {
    content: ""; flex: 1; height: 3px; background: var(--line);
  }

  .field {
    position: absolute; left: 48px; width: 1104px; height: 132px;
    border: 3px solid var(--field-border); border-radius: 16px;
    display: flex; align-items: center; padding: 0 36px;
    font-size: 48px; font-weight: 500; color: var(--placeholder);
  }
  .field.username { top: 1232px; }
  .field.password { top: 1392px; }
  .field .toggle-visibility { position: absolute; right: 34px; top: 36px; }

  .forgot-link {
    position: absolute; right: 48px; top: 1574px;
    font-size: 46px; font-weight: 500; color: var(--ink);
  }

  .login-button {
    position: absolute; left: 48px; top: 1700px; width: 1104px; height: 136px;
    background: var(--brand); border-radius: 12px;
    display: flex; align-items: center; justify-content: center;
    font-size: 50px; font-weight: 700; color: #fff;
  }

  .create-account {
    position: absolute; left: 0; top: 1898px; width: 100%;
    text-align: center; font-size: 48px; font-weight: 600; color: var(--brand-dark);
  }
</style>
</head>
<body>
<main class="screen">
  <div class="status-bar">
    <span class="status-time">9:41</span>
    <svg class="status-icons" width="260" height="48" viewBox="0 0 260 48" aria-hidden="true">
      <g fill="#111">
        <rect x="0" y="30" width="10" height="14" rx="2"/>
        <rect x="16" y="22" width="10" height="22" rx="2"/>
        <rect x="32" y="13" width="10" height="31" rx="2"/>
        <rect x="48" y="4" width="10" height="40" rx="2"/>
        <path d="M110 44 l-9 -10 a13 13 0 0 1 18 0 z"/>
        <path d="M88 22 a32 32 0 0 1 44 0 l-6 6 a24 24 0 0 0 -32 0 z"/>
        <path d="M78 12 a46 46 0 0 1 64 0 l-6 6 a38 38 0 0 0 -52 0 z"/>
        <rect x="166" y="6" width="78" height="38" rx="10" fill="none" stroke="#111" stroke-width="4" opacity="0.45"/>
        <rect x="172" y="12" width="58" height="26" rx="6"/>
        <rect x="249" y="18" width="7" height="14" rx="3" opacity="0.45"/>
      </g>
    </svg>
  </div>

  <div class="brand-name">Tobin Quartz</div>

  <h1 class="page-title">Log in to your<br>account</h1>
  <p class="page-subtitle">Select method to log in:</p>

  <div class="social-row">
    <div class="social-button"><span class="social-dot first"></span>Gravia</div>
    <div class="social-button"><span class="social-dot second"></span>Circlebook</div>
  </div>

  <div class="divider">or continue with</div>

  <div class="field username">Username</div>
  <div class="field password">Password
    <svg class="toggle-visibility" width="64" height="56" viewBox="0 0 64 56" aria-hidden="true">
      <g fill="none" stroke="#333" stroke-width="5" stroke-linecap="round">
        <path d="M4 28 C14 12 50 12 60 28 C50 44 14 44 4 28 Z"/>
        <circle cx="32" cy="28" r="9"/>
        <line x1="8" y1="4" x2="56" y2="52"/>
      </g>
    </svg>
  </div>

  <div class="forgot-link">Forgot password?</div>

  <div class="login-button">Login</div>

  <div class="create-account">Create new account</div>
</main>
</body>
</html>
```